Harborline Energy - needs a business card

Harborline Energy is a U.S. based diesel sourcing and distribution company that supports American oil & gas fields through providing quality product and consistent services.

Target Market(s)

Oil and Gas

Contact Information for Business Card

The background of the card must be white to ensure the logo pops.

Font styles to use
Serif
Sans Serif

Colors

Designer to choose colors to be used in the design.

Requirements
Must have
• Front of Card: Tag line: Harborline Energy, Powering America's Oil & Gas fields.
• Not sure if you guys do this part but just in case...
• Dale Menschow
• Owner/CEO
• C:555.318.4076
• E:Dmenschow@harborlineenergy.example
• W:Harborlineenergy.example
• Locations: Servicing the Powder River, DJ basin and Bakken formations.
• Back of Card: " Frac fueling is what we do. We understand how important diesel fuel is to your operation, which is why our main service line is Frac fueling. We assure our supply and stand by our service"

```html
<!DOCTYPE html>
<html lang="en">
<head>
<meta charset="utf-8">
<title>Harborline Energy – Business Card</title>
<link href="https://fonts.googleapis.com/css2?family=Montserrat:wght@400;600;700&display=swap" rel="stylesheet">
<style>
  :root {
    --navy: #1b2d5b;
    --red: #c0202a;
    --card: #eeeeec;
    --grey-text: #6a6a6a;
    --backdrop: #d6d6d6;
  }
  * { margin: 0; padding: 0; box-sizing: border-box; }
  html, body {
    width: 1200px; height: 1200px; overflow: hidden;
    background: var(--backdrop);
    font-family: 'Montserrat', Arial, sans-serif;
  }
  .card {
    position: absolute;
    left: 226px;
    width: 780px;
    height: 451px;
    background: var(--card);
    overflow: hidden;
  }
  .card-back { top: 106px; }
  .card-front { top: 638px; }

  /* Back of card */
  .brand-mark {
    position: absolute;
    left: 0; right: 0;
    display: flex; flex-direction: column; align-items: center;
  }
  .card-back .brand-mark { top: 92px; }
  .brand-dot {
    width: 64px; height: 64px; border-radius: 50%;
    background: var(--red);
    margin-bottom: 18px;
  }
  .brand-name {
    font-weight: 700;
    color: var(--navy);
    font-size: 28px;
    letter-spacing: 0.5px;
    white-space: nowrap;
  }
  .service-band {
    position: absolute;
    left: 0; right: 0; bottom: 0;
    height: 152px;
    background: var(--navy);
    display: flex; align-items: center; justify-content: center;
  }
  .service-statement {
    width: 640px;
    color: #ffffff;
    font-size: 17.6px;
    line-height: 22.5px;
    text-align: center;
    font-weight: 400;
  }

  /* Front of card */
  .card-front .brand-mark {
    left: 30px; right: auto; width: 320px;
    top: 140px;
  }
  .card-front .brand-name { font-size: 25px; }
  .contact-block {
    position: absolute;
    left: 409px;
    top: 108px;
    width: 360px;
  }
  .person-name {
    font-size: 27px;
    font-weight: 700;
    color: var(--navy);
    line-height: 34px;
    white-space: nowrap;
  }
  .person-name .first { color: var(--red); }
  .person-title {
    font-size: 19px;
    color: var(--red);
    line-height: 24px;
    margin-top: 2px;
  }
  .rule {
    width: 298px;
    height: 2px;
    background: var(--red);
  }
  .rule-top { margin-top: 16px; }
  .service-area {
    font-size: 17.6px;
    line-height: 26px;
    color: var(--grey-text);
    margin: 13px 0 14px;
    white-space: nowrap;
  }
  .contact-list { list-style: none; margin-top: 10px; }
  .contact-list li {
    display: flex; align-items: center;
    font-size: 16.5px;
    line-height: 26px;
    color: var(--grey-text);
    white-space: nowrap;
  }
  .contact-list svg { width: 12px; height: 12px; margin-right: 6px; flex: none; }
  .tagline {
    position: absolute;
    left: 0; right: 0; top: 388px;
    text-align: center;
    font-size: 18.5px;
    color: var(--grey-text);
  }
</style>
</head>
<body>

<section class="card card-back">
  <div class="brand-mark">
    <span class="brand-dot"></span>
    <span class="brand-name">Harborline Energy</span>
  </div>
  <div class="service-band">
    <p class="service-statement">Frac fueling is what we do. We understand how important diesel fuel is to your operation, which is why our main service line is Frac fueling. We assure our supply and stand by our service.</p>
  </div>
</section>

<section class="card card-front">
  <div class="brand-mark">
    <span class="brand-dot"></span>
    <span class="brand-name">Harborline Energy</span>
  </div>

  <div class="contact-block">
    <h1 class="person-name"><span class="first">DALE</span> MENSCHOW</h1>
    <p class="person-title">Owner/CEO</p>
    <div class="rule rule-top"></div>
    <p class="service-area">Servicing the Powder River<br>DJ basin and Bakken formations</p>
    <div class="rule"></div>
    <ul class="contact-list">
      <li>
        <svg viewBox="0 0 12 12" aria-hidden="true"><path d="M2.4 0.8 L4.4 0.8 L5 3.4 L3.7 4.4 C4.4 5.9 5.8 7.4 7.5 8.2 L8.5 6.9 L11.2 7.6 L11.2 9.6 C11.2 10.6 10.4 11.2 9.5 11.2 C4.8 10.8 1.2 7.2 0.8 2.5 C0.8 1.5 1.4 0.8 2.4 0.8 Z" fill="var(--navy)"/></svg>
        555.318.4076
      </li>
      <li>
        <svg viewBox="0 0 12 12" aria-hidden="true"><rect x="0.5" y="2" width="11" height="8" fill="var(--red)"/><path d="M0.5 2 L6 6.5 L11.5 2" stroke="#fff" stroke-width="1" fill="none"/></svg>
        Dmenschow@harborlineenergy.example
      </li>
      <li>
        <svg viewBox="0 0 12 12" aria-hidden="true"><circle cx="6" cy="6" r="5.3" fill="none" stroke="var(--navy)" stroke-width="1.2"/><ellipse cx="6" cy="6" rx="2.3" ry="5.3" fill="none" stroke="var(--navy)" stroke-width="1"/><line x1="0.7" y1="6" x2="11.3" y2="6" stroke="var(--navy)" stroke-width="1"/></svg>
        www.Harborlineenergy.example
      </li>
    </ul>
  </div>

  <p class="tagline">Harborline Energy, Powering America's Oil &amp; Gas fields</p>
</section>

</body>
</html>
```